Removals & Storage a5 brochure required

We require a a4 1 fold into a5 brochure designed. we are an established removals and storage company based in southport, uk. we are looking for somthing we can take into more corporate offices ( estate agents etc) to show off what we do. our website has alot of information : www.haul-and-keep.co.uk which may be of use. we offer Domestic and Commercial removals & storage, packaging sales and services, 24/7 self storage options, mobile self storage. archive storage etc etc i have many files like logos etc where required. nice clean images / hgv with our image superimposed
Target Market(s)
Corporate, estate agents, domestic removals,
Colors
Designer to choose colors to be used in the design.

```html
<!DOCTYPE html>
<html lang="en">
<head>
<meta charset="utf-8">
<title>Harbourside Removals &amp; Storage – A5 Brochure</title>
<link href="https://fonts.googleapis.com/css2?family=Passion+One:wght@400;700&family=Open+Sans:wght@400;600;700&display=swap" rel="stylesheet">
<style>
:root{
  --yellow:#f0b41c;
  --yellow-soft:rgba(240,180,28,.88);
  --charcoal:#333436;
  --charcoal-deep:#2a2b2d;
  --slate:#3b3f42;
  --paper:#f3f3f3;
  --paper-grey:#e4e4e4;
  --ink:#2b2b2b;
  --ink-soft:#555;
  --stage:#b5b5b5;
  --white:#ffffff;
}
*{box-sizing:border-box;margin:0;padding:0}
html,body{width:1079px;height:1200px;overflow:hidden}
body{background:var(--stage);font-family:"Open Sans",Arial,sans-serif;color:var(--ink);position:relative}
.spread{position:absolute;left:124px;width:830px;height:587px;box-shadow:0 6px 18px rgba(0,0,0,.25);overflow:hidden}
.spread--outer{top:8px}
.spread--inner{top:605px}
.page{position:absolute;top:0;width:415px;height:587px;overflow:hidden}
.page--left{left:0}
.page--right{left:415px}
.page svg.bg{position:absolute;inset:0;width:100%;height:100%}
.abs{position:absolute}
.display{font-family:"Passion One","Arial Black",sans-serif;font-weight:700;letter-spacing:.3px}
.photo{position:absolute}
ul{list-style:none}

/* ---------- back cover ---------- */
.back-brand{left:28px;top:36px;display:flex;align-items:center;gap:8px}
.back-brand .mark{width:22px;height:22px;background:var(--charcoal)}
.back-brand .name{font-family:"Passion One",sans-serif;font-size:17px;line-height:.95;color:var(--charcoal);text-transform:uppercase}
.services{left:120px;top:210px;width:280px}
.services h2{font-size:26px;color:var(--charcoal);margin-bottom:4px}
.services li{font-size:11px;color:var(--ink);line-height:1.35;padding-left:12px;position:relative;font-weight:600}
.services li::before{content:"";position:absolute;left:0;top:6px;width:4px;height:4px;border-radius:50%;background:var(--ink)}
.contact{color:var(--white);font-size:10.5px;line-height:1.3}
.contact .icon{position:absolute;left:0;top:2px;width:24px;height:24px;border-radius:50%;background:var(--yellow);display:flex;align-items:center;justify-content:center}
.contact .icon svg{width:12px;height:12px}
.contact .text{padding-left:34px}
.contact--address{left:32px;top:492px}
.contact--phone{left:228px;top:472px}
.contact--email{left:228px;top:514px}

/* ---------- front cover ---------- */
.front-brand{left:120px;top:44px;display:flex;align-items:center;gap:12px}
.front-brand .mark{width:34px;height:34px;background:var(--yellow)}
.front-brand .name{font-family:"Passion One",sans-serif;font-size:28px;line-height:.9;color:var(--white);text-transform:uppercase}
.cover-banner{left:50px;top:345px;width:330px;text-align:center;line-height:1.05}
.cover-banner .l1{font-size:22px;color:var(--white)}
.cover-banner .l2{font-size:22px;color:var(--charcoal)}
.cover-url{left:0;width:415px;top:470px;text-align:center;color:var(--white);font-size:12px;letter-spacing:.4px}

/* ---------- inner left ---------- */
.intro{left:24px;top:26px;width:370px;color:var(--white)}
.intro h2{font-size:22px;color:var(--yellow);margin-bottom:6px}
.intro p{font-size:7.6px;line-height:1.35;margin-bottom:6px;color:#ececec}
.col{width:180px}
.col h3{font-size:18px;color:var(--yellow);margin-bottom:5px}
.col .lede{font-size:8px;color:var(--ink-soft);margin-bottom:6px;line-height:1.3}
.col li{font-size:8px;line-height:1.3;color:var(--ink-soft);padding-left:10px;position:relative}
.col li::before{content:"";position:absolute;left:0;top:4px;width:4px;height:4px;background:var(--yellow)}
.col--home{left:26px;top:302px}
.col--insured{left:214px;top:302px}
.cta{left:24px;top:548px;color:var(--white);font-size:12px;letter-spacing:.3px}
.cta-phone{left:318px;top:540px;font-size:16px;color:var(--charcoal)}

/* ---------- inner right ---------- */
.storage-title{left:22px;top:18px;font-size:20px;color:var(--yellow)}
.storage-col{top:48px;width:118px}
.storage-col h4{font-size:9px;font-weight:700;color:var(--ink);margin-bottom:3px}
.storage-col p{font-size:7.4px;line-height:1.35;color:var(--ink-soft)}
.storage-col--household{left:22px}
.storage-col--commercial{left:150px}
.storage-col--mobile{left:278px}
.archive{left:22px;top:198px;width:375px}
.archive h3{font-size:19px;color:var(--charcoal);margin-bottom:3px}
.archive p{font-size:7.6px;line-height:1.35;color:var(--charcoal)}
.packing{left:22px;top:300px;width:175px;color:var(--white)}
.packing h3{font-size:19px;color:var(--yellow);margin-bottom:4px}
.packing p{font-size:7.6px;line-height:1.4;color:#e6e6e6}
.offers{left:22px;top:410px;width:375px}
.offer{margin-bottom:9px}
.offer h4{font-size:12px;font-weight:400;color:var(--yellow)}
.offer p{font-size:7.6px;line-height:1.35;color:#e6e6e6}
</style>
</head>
<body>

<!-- ================= OUTER SPREAD ================= -->
<section class="spread spread--outer">

  <!-- Back cover -->
  <article class="page page--left back-cover">
    <svg class="bg" viewBox="0 0 415 587" preserveAspectRatio="none">
      <defs>
        <linearGradient id="townhall" x1="0" y1="0" x2="1" y2="1">
          <stop offset="0" stop-color="#c9c9c9"/>
          <stop offset="1" stop-color="#5e5e5e"/>
        </linearGradient>
        <linearGradient id="office" x1="0" y1="0" x2="1" y2="0">
          <stop offset="0" stop-color="#d7d7d7"/>
          <stop offset="1" stop-color="#6a6a6a"/>
        </linearGradient>
      </defs>
      <rect width="415" height="587" fill="#ececec"/>
      <polygon points="0,120 170,80 130,470 0,470" fill="url(#townhall)" role="img" aria-label="Black and white photo of a historic town hall building"/>
      <polygon points="160,60 415,0 415,140 335,470 0,470 0,400 120,140" fill="var(--yellow-soft)"/>
      <polygon points="380,0 415,0 415,30" fill="var(--yellow)"/>
      <polygon points="175,58 405,25 405,105 150,185" fill="url(#office)" role="img" aria-label="Black and white photo of an empty office with desks and shelving"/>
      <polygon points="0,470 415,420 415,587 0,587" fill="var(--charcoal)"/>
    </svg>

    <div class="abs back-brand">
      <span class="mark"></span>
      <span class="name">Harbourside<br>Removals<br>&amp; Storage</span>
    </div>

    <div class="abs services">
      <h2 class="display">Services</h2>
      <ul>
        <li>Domestic removals</li>
        <li>Commercial relocations</li>
        <li>Worldwide shipping management</li>
        <li>Part loads nationwide</li>
        <li>Specialist antique, piano and heavy item transportation</li>
        <li>Domestic and commercial storage</li>
        <li>Dismantling and reassembling of furniture</li>
        <li>Full / Part packing / unpacking services</li>
        <li>Boxes and packaging materials</li>
        <li>Clearance, collection and disposal services</li>
        <li>Courier service</li>
      </ul>
    </div>

    <div class="abs contact contact--address">
      <span class="icon"><svg viewBox="0 0 12 12"><path d="M6 1 1 5.5h1.5V11h2.5V7.5h2V11h2.5V5.5H11z" fill="#333436"/></svg></span>
      <div class="text">Address<br>Unit 4,<br>Larkfield Yard,<br>Millbrook Trading Park<br>ZZ1 4QT</div>
    </div>
    <div class="abs contact contact--phone">
      <span class="icon"><svg viewBox="0 0 12 12"><path d="M3 1.5 4.6 1l1 2.6-1.1.9a6 6 0 0 0 3 3l.9-1.1 2.6 1-.5 1.6C8.5 10.5 1.5 3.5 3 1.5z" fill="#333436"/></svg></span>
      <div class="text">Phone<br>01632 960 418</div>
    </div>
    <div class="abs contact contact--email">
      <span class="icon"><svg viewBox="0 0 12 12"><rect x="1" y="3" width="10" height="7" fill="#333436"/><path d="M1 3.3 6 7l5-3.7" stroke="#f0b41c" stroke-width="1" fill="none"/></svg></span>
      <div class="text">Email<br>hello@haul-and-keep.co.uk</div>
    </div>
  </article>

  <!-- Front cover -->
  <article class="page page--right front-cover">
    <svg class="bg" viewBox="0 0 415 587" preserveAspectRatio="none">
      <defs>
        <linearGradient id="van" x1="0" y1="0" x2="1" y2="1">
          <stop offset="0" stop-color="#9a9a9a"/>
          <stop offset=".45" stop-color="#ededed"/>
          <stop offset="1" stop-color="#4f4f4f"/>
        </linearGradient>
      </defs>
      <rect width="415" height="587" fill="var(--charcoal)"/>
      <polygon points="0,0 40,0 0,120" fill="var(--yellow)"/>
      <polygon points="80,140 415,125 415,150 110,165" fill="var(--yellow)"/>
      <rect x="0" y="165" width="415" height="185" fill="url(#van)" role="img" aria-label="Photo of a white removals lorry with company livery"/>
      <polygon points="0,165 30,165 0,230" fill="var(--yellow)"/>
      <polygon points="40,335 400,320 395,395 30,412" fill="var(--yellow)"/>
    </svg>

    <div class="abs front-brand">
      <span class="mark"></span>
      <span class="name">Harbourside<br>Removals<br>&amp; Storage</span>
    </div>

    <div class="abs cover-banner display">
      <div class="l1">DOMESTIC AND COMMERCIAL</div>
      <div class="l2">REMOVALS &amp; STORAGE</div>
    </div>

    <div class="abs cover-url">www.haul-and-keep.co.uk</div>
  </article>
</section>

<!-- ================= INNER SPREAD ================= -->
<section class="spread spread--inner">

  <!-- Inner left -->
  <article class="page page--left inner-left">
    <svg class="bg" viewBox="0 0 415 587" preserveAspectRatio="none">
      <defs>
        <linearGradient id="home" x1="0" y1="0" x2="1" y2="1">
          <stop offset="0" stop-color="#a8573d"/>
          <stop offset=".6" stop-color="#c9ad86"/>
          <stop offset="1" stop-color="#6d8a3e"/>
        </linearGradient>
        <linearGradient id="officeColour" x1="0" y1="0" x2="1" y2="0">
          <stop offset="0" stop-color="#b9b4ae"/>
          <stop offset=".5" stop-color="#8a6552"/>
          <stop offset="1" stop-color="#6f4b3c"/>
        </linearGradient>
      </defs>
      <rect width="415" height="587" fill="var(--paper)"/>
      <rect width="415" height="165" fill="var(--charcoal)"/>
      <polygon points="0,0 160,0 140,18 0,18" fill="var(--yellow)"/>
      <rect x="26" y="180" width="172" height="98" fill="url(#home)" role="img" aria-label="Photo of movers carrying boxes out of a brick house"/>
      <rect x="212" y="180" width="178" height="98" fill="url(#officeColour)" role="img" aria-label="Photo of an office with wooden shelving and desks"/>
      <rect x="0" y="530" width="415" height="40" fill="var(--charcoal)"/>
      <polygon points="335,440 415,440 415,587 300,587" fill="var(--yellow)"/>
    </svg>

    <div class="abs intro">
      <h2 class="display">Harbourside Removals and Storage</h2>
      <p>Harbourside Removals and Storage provides seamless house removal and commercial business moves throughout the North west and nationwide.</p>
      <p>With more than two decades of experience within the moving and storage industry, Harbourside Removals and Storage provides a reliable, efficient service, ensuring our customers receive a quality service every time.</p>
      <p>In addition to our home, business and office removals we also provide other services such as storage solutions, packing services, antique and piano transportation.</p>
    </div>

    <div class="abs col col--home">
      <h3 class="display">Home removal services</h3>
      <p class="lede">Our range of home removal services include ...</p>
      <ul>
        <li>Packing services</li>
        <li>Specialist antique and piano transportation</li>
        <li>Estate clearance service</li>
        <li>Removal and disposal of unwanted items</li>
        <li>Furniture dismantling and reassembly</li>
        <li>Export wrapping</li>
        <li>Storage</li>
        <li>Internal moves within your home</li>
        <li>Cleaning service</li>
        <li>Moving abroad</li>
      </ul>
    </div>

    <div class="abs col col--insured">
      <h3 class="display">Fully-insured movers</h3>
      <p class="lede">Other commercial services undertaken...</p>
      <ul>
        <li>Tower block relocation logistics multiple occupancy</li>
        <li>Crate rental</li>
        <li>Courier services</li>
        <li>Relocation of safes and heavy items (including lathes, large printers, commercial kitchens)</li>
        <li>Internal moves</li>
        <li>Transportation of confidential materials</li>
        <li>Storage</li>
        <li>Removal and disposal of unwanted items</li>
      </ul>
    </div>

    <div class="abs cta">Call us to arrange a free no obligation quotation on</div>
    <div class="abs cta-phone display">01632 960 418</div>
  </article>

  <!-- Inner right -->
  <article class="page page--right inner-right">
    <svg class="bg" viewBox="0 0 415 587" preserveAspectRatio="none">
      <defs>
        <linearGradient id="boxes" x1="0" y1="0" x2="1" y2="1">
          <stop offset="0" stop-color="#e8e2d6"/>
          <stop offset=".5" stop-color="#c89a64"/>
          <stop offset="1" stop-color="#a8773f"/>
        </linearGradient>
      </defs>
      <rect width="415" height="587" fill="var(--paper)"/>
      <polygon points="0,185 415,160 415,270 0,300" fill="var(--yellow)"/>
      <polygon points="0,300 415,270 415,587 0,587" fill="var(--slate)"/>
      <polygon points="210,290 415,275 415,390 240,400" fill="url(#boxes)" role="img" aria-label="Photo of stacked cardboard moving boxes in a living room"/>
      <polygon points="360,275 400,275 380,390 345,392" fill="var(--yellow-soft)"/>
      <polygon points="260,565 415,545 415,587 250,587" fill="var(--yellow)"/>
    </svg>

    <h2 class="abs storage-title display">Storage solutions</h2>
    <div class="abs storage-col storage-col--household">
      <h4>Household Storage</h4>
      <p>Harbourside Removals and Storage provides clean, dry secure storage for all your household furniture and goods. Our storage facilities are safe and secure with 24 hour CCTV and alarmed to give you peace of mind that your goods are safe with us.</p>
    </div>
    <div class="abs storage-col storage-col--commercial">
      <h4>Commercial Storage</h4>
      <p>Harbourside Removals and Storage offers flexible storage solutions for businesses of all sizes, our services are tailor made to suit the changing needs of our customers. Our storage solutions are ideal for either long term or short term storage of stock, office equipment, palletised stock and archive storage.</p>
    </div>
    <div class="abs storage-col storage-col--mobile">
      <h4>Mobile Self Storage</h4>
      <p>Mobile Self Storage is a convenient, hassle free, simple way to store your goods. We deliver a mobile storage unit directly to your home or business, you load your goods into the storage unit then we take it away to our storage facility and store it.</p>
    </div>

    <div class="abs archive">
      <h3 class="display">Archive Storage</h3>
      <p>Do you need an off-site archive solution to store your company's files? Many company documents need to be stored for a number of years. Why have this burden, let us do it for you. We can deliver individual files and boxes at your request any time as and when you need them.</p>
    </div>

    <div class="abs packing">
      <h3 class="display">Packing Service</h3>
      <p>Here at Harbourside Removals and Storage, we can assist you by providing a flexible packing service to suit your needs and budget, our range of packing services ensure you get the help you require, at a cost you'll love</p>
    </div>

    <div class="abs offers">
      <div class="offer">
        <h4>Full Packing Service</h4>
        <p>Leaving all your packing to us, we will come and pack your entire home ready for your move.</p>
      </div>
      <div class="offer">
        <h4>Part Packing Service</h4>
        <p>Packing of breakables from crockery, precious glassware and ornaments, to your heavier items such as books, collectables and tools.</p>
      </div>
      <div class="offer">
        <h4>Export Wrapping</h4>
        <p>We will export wrap selected items, such as antiques, paintings, pictures and high finish furniture for transport, local or long distance.</p>
      </div>
    </div>
  </article>
</section>

</body>
</html>
```